Kveldbrá - Start-up company selling electricity

Hello let me tell you about Kveldbrá.

Kveldbrá is start-up company selling electricity in Iceland. The operations of the company consist of making power usage forecasts for our customers, purchasing the electricity wholesale from the energy producers, and selling the electricity to the consumer. We are focused on tech by using optimization and machine learning to minimize electricity prices to our customers. Our marketing strategy is to portray a tech company mindset and to show dedication to driving down the electricity price on the market.

We need your help to make our website pop. Possible concepts to work with are as follows:

- Iceland the land of ice and fire
- Green energy
- Innovation
- Tech and data science

Link to our website: https://prufa.kveldbra.is/
We are open to ideas.
Thank you!

Target Market(s)

Electricity consumers both homes and companies.

Number of Pages Required

1 page

Font styles to use
Serif
Sans Serif

```html
<!DOCTYPE html>
<html lang="en">
<head>
<meta charset="utf-8">
<title>Kveldbrá – Same Electricity, Just Cheaper</title>
<link href="https://fonts.googleapis.com/css2?family=Audiowide&family=Noto+Serif:wght@400;700&family=Poppins:wght@400&family=Source+Sans+3:wght@400;600&display=swap" rel="stylesheet">
<style>
:root{
  --red:#a8332b;
  --red-deep:#8e2520;
  --navy:#1d3563;
  --navy-deep:#17294f;
  --ink:#2b2b2b;
  --muted:#5d5d5d;
  --paper:#ffffff;
  --mist:#f4f6f8;
  --serif:'Noto Serif', Georgia, serif;
  --sans:'Source Sans 3', Arial, sans-serif;
}
*{box-sizing:border-box;margin:0;padding:0}
html,body{width:1200px;height:2794px;overflow:hidden;background:var(--paper)}
.page{position:relative;width:1200px;height:2794px;overflow:hidden;font-family:var(--sans);color:var(--ink)}
.abs{position:absolute}

/* header */
.brand{position:absolute;display:flex;align-items:center;gap:10px;font-family:var(--serif);font-weight:700;letter-spacing:.5px;white-space:nowrap}
.brand-dot{width:26px;height:26px;border-radius:50%;background:currentColor}
.site-brand{left:60px;top:28px;color:#fff;font-size:28px}
.main-nav{position:absolute;right:126px;top:35px;display:flex;gap:22px;font-size:13px;color:#fff;white-space:nowrap}
.lang{position:absolute;left:1096px;top:29px;width:45px;height:24px;border:1px solid #fff;border-radius:3px;color:#fff;font-size:12px;padding:3px 8px}
.lang::after{content:"";position:absolute;right:7px;top:10px;border:4px solid transparent;border-top-color:#fff}

/* hero */
.hero-art{position:absolute;left:0;top:0}
.hero-title{position:absolute;left:0;width:1200px;top:214px;text-align:center;font-family:'Audiowide',sans-serif;font-weight:400;font-size:60px;line-height:84px;color:#fff;-webkit-text-stroke:2px var(--navy);white-space:nowrap}
.hero-sub{position:absolute;left:336px;top:398px;width:534px;height:37px;background:rgba(29,53,99,.55);color:#fff;font-family:'Poppins',sans-serif;font-size:14px;line-height:37px;text-align:center;white-space:nowrap}
.arrow-btn{position:absolute;top:321px;width:42px;height:42px;border:1px solid rgba(255,255,255,.8);border-radius:50%}
.arrow-btn svg{display:block}
.dots{position:absolute;top:687px;left:561px;display:flex;gap:7px}
.dots span{width:11px;height:11px;border:1px solid #fff;border-radius:50%}
.dots .on{background:var(--red);box-shadow:0 0 0 2px #fff inset}

/* buttons */
.pill{position:absolute;display:flex;align-items:center;justify-content:space-between;gap:10px;height:38px;border-radius:19px;background:var(--red);color:#fff;font-family:var(--serif);font-size:14px;line-height:1;padding:0 3px 0 18px;letter-spacing:.2px;white-space:nowrap}
.pill i{flex:none;width:32px;height:32px;border-radius:50%;background:#fff;box-shadow:inset 0 0 0 8px #fff,inset 0 0 0 16px var(--navy)}
.pill.navy{background:var(--navy)}

/* headings */
.kicker{font-family:var(--serif);font-weight:400;color:var(--red);font-size:36px;line-height:42px}
.lead{font-family:var(--serif);font-weight:700;color:var(--navy);font-size:36px;line-height:42px}
.rule{position:absolute;height:1px;background:var(--red);opacity:.9}
.rule b{position:absolute;left:0;top:-2px;height:5px;background:var(--red)}

/* about */
.about-text{position:absolute;left:174px;top:844px;width:392px}
.about-q{font-family:var(--serif);font-size:15px;line-height:21px;margin-top:26px;color:var(--ink)}
.body-copy{font-size:13px;line-height:21px;color:var(--muted);margin-top:10px}
.cycle{position:absolute;left:0;top:800px}
.node{position:absolute;width:110px;height:110px;border-radius:50%;background:#fff;box-shadow:0 3px 14px rgba(0,0,0,.15)}
.node div{position:absolute;inset:14px;border-radius:50%}
.node-label{position:absolute;font-family:var(--serif);font-weight:700;color:var(--red);font-size:16px;white-space:nowrap}

/* pricing */
.band-mist{position:absolute;left:0;top:1305px;width:1200px;height:760px;background:var(--mist)}
.section-head{position:absolute;left:495px;top:1375px;white-space:nowrap}
.card{position:absolute;top:1542px;width:268px;height:436px;background:#fff;border-radius:8px;box-shadow:0 4px 16px rgba(0,0,0,.12);text-align:center}
.card .photo{position:absolute;left:8px;top:8px;width:252px;height:165px;border-radius:4px}
.card h3{position:absolute;top:200px;width:100%;font-family:var(--serif);font-weight:700;font-size:18px;color:var(--navy);white-space:nowrap}
.price{font-family:var(--serif);font-size:26px;color:var(--red);line-height:28px}
.unit{font-size:12px;color:var(--muted);line-height:14px}

/* talk */
.talk-text{position:absolute;left:617px;top:2166px;width:380px}
.talk-text .kicker,.talk-text .lead{font-size:33px;line-height:41px}

/* footer */
.footer-art{position:absolute;left:0;top:2490px}
.foot-col{position:absolute;top:2592px;color:#fff;font-size:12px;white-space:nowrap}
.foot-col h4{font-family:var(--serif);font-weight:700;font-size:16px;margin-bottom:16px}
.foot-col li{list-style:none;position:relative;padding-left:18px;line-height:25px}
.foot-col li::before{content:"";position:absolute;left:0;top:11px;width:5px;height:5px;border-radius:50%;background:var(--red)}
.contact li::before{display:none}
.contact li{padding-left:27px}
.contact svg{position:absolute;left:0;top:5px}
.footer-brand{left:70px;top:2645px;font-size:30px;font-weight:400;color:var(--red)}
.copyright{position:absolute;top:2762px;width:1200px;text-align:center;color:#c9d1e0;font-size:12px}
</style>
</head>
<body>
<main class="page">

  <!-- hero -->
  <svg class="hero-art" width="1200" height="740" viewBox="0 0 1106 682" preserveAspectRatio="none" role="img" aria-label="Aerial view of a geothermal plant and a glowing lava flow in red and navy tones">
    <defs>
      <clipPath id="heroClip"><path d="M0 0H1106V555Q553 809 0 555Z"/></clipPath>
      <linearGradient id="heroRed" x1="0" y1="0" x2="1" y2="1">
        <stop offset="0" stop-color="#b0443a"/><stop offset="1" stop-color="#9c2e26"/>
      </linearGradient>
      <linearGradient id="heroNavy" x1="0" y1="0" x2="0" y2="1">
        <stop offset="0" stop-color="#2a4472"/><stop offset="1" stop-color="#1f3663"/>
      </linearGradient>
    </defs>
    <g clip-path="url(#heroClip)">
      <rect width="1106" height="682" fill="url(#heroRed)"/>
      <polygon points="0,115 560,398 540,682 0,682" fill="#fff"/>
      <polygon points="0,178 560,420 540,682 0,682" fill="url(#heroNavy)"/>
      <polygon points="483,175 1106,555 1106,682 540,682 540,400" fill="#fff"/>
      <polygon points="483,200 1106,580 1106,682 540,682 540,420" fill="url(#heroNavy)"/>
      <path d="M260 420Q420 470 560 480T820 470" stroke="#a8332b" stroke-width="16" fill="none" opacity=".55"/>
    </g>
  </svg>

  <div class="brand site-brand"><span class="brand-dot"></span>KVELDBRÁ</div>
  <nav class="main-nav"><span>Terms of Business</span><span>Question &amp; Answer</span><span>About Kveldbrá</span></nav>
  <div class="lang">En</div>

  <div class="arrow-btn" style="left:60px"><svg width="40" height="40"><path d="M23 12l-8 8 8 8" stroke="#fff" fill="none" stroke-width="1.5"/></svg></div>
  <div class="arrow-btn" style="left:1098px"><svg width="40" height="40"><path d="M17 12l8 8-8 8" stroke="#fff" fill="none" stroke-width="1.5"/></svg></div>

  <h1 class="hero-title">Selling And<br>Generating Energy</h1>
  <p class="hero-sub">Everything you need to know about how we can help you sell electricity</p>
  <div class="pill" style="left:518px;top:450px;width:164px">GET A QUOTE<i></i></div>
  <div class="dots"><span></span><span class="on"></span><span></span><span></span><span></span></div>

  <!-- about -->
  <section class="about-text">
    <h2 class="kicker">About</h2>
    <h2 class="lead">Kveldbrá</h2>
    <div class="rule" style="left:0;top:91px;width:106px"><b style="width:44px"></b></div>
    <p class="about-q">What is Kveldbrá's unique position in the electricity sales market?</p>
    <p class="body-copy">Kveldbrá uses automation and artificial intelligence to achieve lower prices in the electricity market. Our goal is to minimize the cost of energy sales, promote energy balance and offer good service.</p>
    <p class="body-copy">Kveldbrá's goal is to offer its customers the most favorable electricity prices in Iceland. Electricity is part of the monthly costs of households and companies, and by doing business with Kveldbrá, savings can be achieved and operating costs reduced.</p>
  </section>
  <div class="pill" style="left:174px;top:1174px;width:150px">LEARN MORE<i></i></div>

  <svg class="cycle" width="1200" height="460">
    <circle cx="868" cy="193" r="174" fill="none" stroke="#8a8a8a" stroke-dasharray="2 3"/>
    <path d="M900 22l12-5-6 12z" fill="var(--navy)"/>
    <path d="M695 248l12 4-10 8z" fill="var(--navy)"/>
    <path d="M980 323l12-2-4 12z" fill="var(--navy)"/>
    <circle cx="872" cy="183" r="72" fill="var(--navy)" opacity=".92" role="img" aria-label="Energy emblem"/>
  </svg>
  <div class="node" style="left:664px;top:852px"><div style="background:linear-gradient(135deg,#dfe6ee,#8fa3b8)" role="img" aria-label="Power plant illustration"></div></div>
  <div class="node-label" style="left:656px;top:976px">Generator</div>
  <div class="node" style="left:968px;top:890px"><div style="background:linear-gradient(135deg,#cfe6c2,#6fb24e)" role="img" aria-label="Home customer illustration"></div></div>
  <div class="node-label" style="left:1004px;top:1010px">Customer</div>
  <div class="node" style="left:757px;top:1100px"><div style="background:linear-gradient(135deg,#e6ece6,#9cc48a)" role="img" aria-label="Reseller office illustration"></div></div>
  <div class="node-label" style="left:783px;top:1216px">Reseller</div>

  <!-- pricing -->
  <div class="band-mist"></div>
  <svg class="abs" style="left:0;top:1640px" width="1200" height="420" viewBox="0 0 1200 420" preserveAspectRatio="none" role="img" aria-label="Red-toned aerial photo of a lava field">
    <defs><linearGradient id="lava" x1="0" y1="0" x2="0" y2="1"><stop offset="0" stop-color="#b23b31"/><stop offset="1" stop-color="#952a23"/></linearGradient></defs>
    <path d="M0 4Q600 220 1200 4V420H0Z" fill="url(#lava)"/>
  </svg>

  <div class="section-head">
    <h2 class="kicker">Same Electricity</h2>
    <h2 class="lead">~ Just Cheaper!</h2>
  </div>
  <div class="rule" style="left:526px;top:1482px;width:104px"><b style="width:42px"></b></div>

  <article class="card" style="left:175px">
    <div class="photo" style="background:linear-gradient(180deg,#9fb0c0 0%,#c9ced2 40%,#6d7b3e 70%,#4c5a2a 100%)" role="img" aria-label="Geothermal power station in a green landscape"></div>
    <h3>Welcome To Business</h3>
  </article>
  <div class="pill" style="left:237px;top:1777px;width:143px">REGISTER<i></i></div>

  <article class="card" style="left:465px">
    <div class="photo" style="background:linear-gradient(180deg,#5f7fa8 0%,#c9d6e6 45%,#e8eef4 70%,#8a9bb0 100%)" role="img" aria-label="Hydropower station in snow with power lines"></div>
    <h3>Price List</h3>
    <div class="abs" style="top:238px;width:100%">
      <p class="price">6.95</p><p class="unit">ISK/kWh</p>
      <p class="price" style="margin-top:18px">6.22</p><p class="unit">ISK/kWh</p>
      <p class="unit" style="margin-top:20px;font-size:13px">electric acceleration</p>
      <p style="font-size:14px;margin-top:6px;color:#333">Make a price comparison</p>
    </div>
  </article>

  <article class="card" style="left:756px">
    <div class="photo" style="background:radial-gradient(circle at 60% 40%,#bfd4ff 0%,#3b63b8 30%,#13265a 80%)" role="img" aria-label="Glowing data network visual"></div>
    <h3>The Future Is Exciting</h3>
    <p class="body-copy abs" style="top:240px;left:32px;width:204px;margin-top:0">Let's make the electricity system smarter together. Kveldbrá uses artificial intelligence, data science and automation to minimize costs and promote eccentricity</p>
  </article>

  <div class="pill navy" style="left:525px;top:2040px;width:150px">VERÐVAKI<i></i></div>

  <!-- talk -->
  <div class="abs" style="left:176px;top:2180px;width:200px;height:230px;border-radius:50%;background:#e7ebf1"></div>
  <div class="abs" style="left:262px;top:2105px;width:254px;height:412px;border-radius:90px 90px 10px 10px;background:linear-gradient(180deg,#d9d9d9 0%,#3a3a3a 40%,#1d1d1d 100%)" role="img" aria-label="Thoughtful businessman in a dark suit"></div>
  <section class="talk-text">
    <h2 class="kicker">Want To Talk</h2>
    <h2 class="lead">About Buying Your Energy?</h2>
    <p class="body-copy" style="margin-top:14px;font-size:13.5px;line-height:23px">The operations of the company consist of making power usage forecasts for our customers, purchasing the electricity wholesale from the energy producers, and selling the electricity</p>
  </section>
  <div class="pill" style="left:617px;top:2390px;width:165px">REGISTER NOW<i></i></div>

  <!-- footer -->
  <svg class="footer-art" width="1200" height="304" viewBox="0 0 1200 304" preserveAspectRatio="none">
    <path d="M0 75Q600 -35 1200 75V304H0Z" fill="var(--navy-deep)"/>
    <path d="M0 75Q600 -35 1200 75" fill="none" stroke="var(--red)" stroke-width="4"/>
    <circle cx="600" cy="22" r="31" fill="var(--red)"/>
    <circle cx="600" cy="22" r="18" fill="#fff"/>
    <line x1="60" y1="255" x2="1140" y2="255" stroke="#33497a"/>
  </svg>

  <div class="brand footer-brand"><span class="brand-dot" style="background:#fff"></span>KVELDBRÁ</div>

  <div class="foot-col" style="left:336px">
    <h4>Sitemap</h4>
    <ul><li>Terms of Business</li><li>Question &amp; Answer</li><li>About Kveldbrá</li></ul>
  </div>
  <div class="foot-col contact" style="left:612px">
    <h4>Contact Us</h4>
    <ul>
      <li><svg width="14" height="16"><path d="M7 1a5 5 0 0 1 5 5c0 4-5 9-5 9S2 10 2 6a5 5 0 0 1 5-5z" fill="none" stroke="var(--red)" stroke-width="1.6"/><circle cx="7" cy="6" r="1.8" fill="var(--red)"/></svg>Hrímgata 8 210 Lindarbær</li>
      <li style="margin-top:4px"><svg width="14" height="12"><rect x="1" y="1" width="12" height="10" rx="1" fill="var(--red)"/><path d="M1 2l6 5 6-5" stroke="#fff" fill="none"/></svg>kveldbra@kveldbra.is</li>
      <li style="margin-top:4px;font-size:17px"><svg width="14" height="16"><path d="M3 1l3 3-2 2a9 9 0 0 0 5 5l2-2 3 3-2 2C6 14 1 9 1 3z" fill="var(--red)"/></svg>555-0199</li>
    </ul>
  </div>
  <div class="foot-col" style="left:888px">
    <h4>More Info</h4>
    <ul><li>Kveldbrá ehf</li><li>ID number: 610321-0470</li><li>VAT number: 204731</li></ul>
  </div>

  <p class="copyright">©Kveldbrá - 2021 all right rserved.</p>
</main>
</body>
</html>
```